Graphic Design Template for Digital Marketing Strategy

I require a template designing for a digital marketing strategy template, this will be a downloadable 2 page pdf.

One side will have a diagram showcasing all relevant DM strategies and how businesses should implement them, the following page will have a table that helps in the planning process.

I will provide all the content, however I need it to look professional, more importantly I need it to be a usable document for a business that lacks DM knowledge, so it needs to have implementable steps!

I have attached a similar document, this is good, however it does not get across the steps needs to be taken.

Also attached our logo.

Any questions please ask.

Dale

Digital

```html
<!DOCTYPE html>
<html lang="en">
<head>
<meta charset="utf-8">
<title>Identify Your Target Market</title>
<link rel="stylesheet" href="https://fonts.googleapis.com/css2?family=Open+Sans:wght@400;700&family=Roboto+Condensed:wght@700&display=swap">
<style>
  :root {
    --page-top: #f6f7f9;
    --page-mid: #eceef1;
    --ink: #404448;
    --title-blue: #1161a8;
    --bar-blue: #0b79b3;
    --wave-light: #29a3df;
    --wave-dark: #0d6cae;
    --tab-grey: #9aa6b2;
    --footer-ink: #5a5e62;
    --brand-ink: #1d2a36;
    --white: #ffffff;
  }
  * { margin: 0; padding: 0; box-sizing: border-box; }
  html, body { width: 1200px; height: 849px; overflow: hidden; background: var(--white); }
  .page {
    position: relative;
    width: 1200px;
    height: 849px;
    overflow: hidden;
    background: radial-gradient(ellipse 70% 60% at 45% 45%, var(--white) 0%, var(--page-top) 55%, var(--page-mid) 100%);
    font-family: "Open Sans", Arial, sans-serif;
  }
  .title-tab {
    position: absolute; left: 0; top: 66px; width: 50px; height: 24px;
    background: linear-gradient(90deg, #c3cad2, var(--tab-grey));
  }
  .page-title {
    position: absolute; left: 58px; top: 57px;
    font-family: "Roboto Condensed", "Arial Narrow", sans-serif;
    font-weight: 700; font-size: 33px; letter-spacing: -1px;
    color: var(--title-blue);
  }
  .step { position: absolute; width: 530px; }
  .step-left { left: 53px; }
  .step-right { left: 617px; }
  .row-1 { top: 141px; }
  .row-2 { top: 315px; }
  .row-3 { top: 489px; }
  .step-heading {
    height: 38px; background: var(--bar-blue); color: var(--white);
    font-weight: 700; font-size: 20px; line-height: 38px; padding-left: 24px;
    letter-spacing: -0.2px;
  }
  .step-text {
    margin-top: 16px; padding-left: 25px; width: 505px;
    font-size: 16.4px; line-height: 23.5px; color: var(--ink);
    letter-spacing: -0.1px;
  }
  .wave { position: absolute; left: 0; top: 680px; width: 1200px; height: 80px; }
  .footer-bg { position: absolute; left: 0; top: 740px; width: 1200px; height: 109px; background: var(--white); }
  .footer-note {
    position: absolute; left: 50px; top: 797px;
    font-family: Arial, Helvetica, sans-serif; font-size: 11px; color: var(--footer-ink);
  }
  .brand {
    position: absolute; right: 40px; top: 788px;
    display: flex; align-items: center; gap: 10px;
  }
  .brand-dot { width: 34px; height: 34px; border-radius: 50%; background: var(--wave-light); }
  .brand-name {
    font-family: "Open Sans", Arial, sans-serif; font-weight: 700; font-size: 14px;
    line-height: 15px; color: var(--brand-ink); text-align: center; letter-spacing: 0.5px;
  }
</style>
</head>
<body>
<main class="page">
  <div class="title-tab"></div>
  <h1 class="page-title">Identify Your Target Market</h1>

  <section class="step step-left row-1">
    <h2 class="step-heading">Hypothesize</h2>
    <p class="step-text">Lorem ipsum dolor sit amet, consectetur adipisicing elit, sed do eiusmod tempor incididunt ut labore et dolore magna aliqua. Ut enim ad minim veniam,</p>
  </section>
  <section class="step step-right row-1">
    <h2 class="step-heading">Contextualise</h2>
    <p class="step-text">Lorem ipsum dolor sit amet, consectetur adipisicing elit, sed do eiusmod tempor incididunt ut labore et dolore magna aliqua. Ut enim ad minim veniam,</p>
  </section>
  <section class="step step-left row-2">
    <h2 class="step-heading">Discover</h2>
    <p class="step-text">Lorem ipsum dolor sit amet, consectetur adipisicing elit, sed do eiusmod tempor incididunt ut labore et dolore magna aliqua. Ut enim ad minim veniam,</p>
  </section>
  <section class="step step-right row-2">
    <h2 class="step-heading">Act</h2>
    <p class="step-text">Lorem ipsum dolor sit amet, consectetur adipisicing elit, sed do eiusmod tempor incididunt ut labore et dolore magna aliqua. Ut enim ad minim veniam,</p>
  </section>
  <section class="step step-left row-3">
    <h2 class="step-heading">Define</h2>
    <p class="step-text">Lorem ipsum dolor sit amet, consectetur adipisicing elit, sed do eiusmod tempor incididunt ut labore et dolore magna aliqua. Ut enim ad minim veniam,</p>
  </section>
  <section class="step step-right row-3">
    <h2 class="step-heading">Listen</h2>
    <p class="step-text">Lorem ipsum dolor sit amet, consectetur adipisicing elit, sed do eiusmod tempor incididunt ut labore et dolore magna aliqua. Ut enim ad minim veniam,</p>
  </section>

  <div class="footer-bg"></div>
  <svg class="wave" viewBox="0 680 1200 80" aria-hidden="true">
    <path d="M0,695 Q600,716 1200,692 L1200,740 L0,740 Z" fill="var(--wave-light)"/>
    <path d="M0,714 Q600,724 1200,704 L1200,716 Q600,732 0,742 Z" fill="var(--wave-dark)"/>
    <path d="M0,742 Q600,732 1200,716 L1200,760 L0,760 Z" fill="var(--white)"/>
  </svg>

  <p class="footer-note">©Brightlane Digital www.brightlanedigital.com</p>

  <div class="brand">
    <span class="brand-dot"></span>
    <span class="brand-name">BRIGHTLANE<br>DIGITAL</span>
  </div>
</main>
</body>
</html>
```